TWL Business Card Design Project

Real Estate Broker, plain badge shape
I would like something similar to what I have attached from Corvell Realty except my company is Marlow Realty Group, LLC. Instead of a single "M" on the back I would like "TWL". Phone # 816-552-4917
Name - Dorian Faulk
Licensed in the State of Missouri
No address
email - dfaulk@marlowhomesexample.com
Contact Information for Business Card
I would like something similar to what I have attached from Corvell Realty except my company is Marlow Realty Group, LLC. Instead of a single "M" on the back I would like "TWL". Phone # 816-863-8328Name - Jeremy YiLicensed in the State of MissouriNo addressemail - dfaulk@marlowhomesexample.com

```html
<!DOCTYPE html>
<html lang="en">
<head>
<meta charset="utf-8">
<title>Marlow Realty Group – Business Card</title>
<link rel="stylesheet" href="https://fonts.googleapis.com/css2?family=Cinzel:wght@400;600&family=Montserrat:wght@300;400;600;700&display=swap">
<style>
  :root {
    --stage: #d1d2d4;
    --espresso: #3e382e;
    --sky: #48aed8;
    --white: #ffffff;
    --rule: #b9b6b0;
  }
  * { margin: 0; padding: 0; box-sizing: border-box; }
  html, body { width: 1200px; height: 1000px; overflow: hidden; }
  body {
    background: var(--stage);
    position: relative;
    font-family: "Montserrat", Arial, sans-serif;
  }
  .card {
    position: absolute;
    top: 201px;
    width: 342px;
    height: 598px;
    box-shadow: 6px 7px 8px rgba(0,0,0,0.28);
  }
  .card--front { left: 229px; background: var(--espresso); }
  .card--back { left: 630px; background: var(--sky); }
  .centered { position: absolute; left: 0; width: 100%; text-align: center; }

  .brand-dot {
    position: absolute; left: 140px; top: 23px;
    width: 62px; height: 62px; border-radius: 50%;
    background: var(--sky);
  }
  .brand-dot span {
    display: block; line-height: 62px; text-align: center;
    font-family: "Cinzel", Georgia, serif; font-weight: 600;
    font-size: 20px; color: var(--espresso);
  }
  .brand-name {
    top: 88px; font-family: "Cinzel", Georgia, serif; font-weight: 400;
    color: var(--white); font-size: 46px; letter-spacing: 4px; line-height: 54px;
  }
  .brand-sub {
    top: 144px; font-family: "Cinzel", Georgia, serif; font-weight: 400;
    color: var(--white); font-size: 30px; line-height: 36px;
  }
  .brand-llc {
    position: absolute; top: 187px; left: 38px; width: 266px;
    display: flex; align-items: center; gap: 10px;
    font-family: "Cinzel", Georgia, serif; color: var(--white); font-size: 15px;
  }
  .brand-llc::before, .brand-llc::after {
    content: ""; flex: 1; height: 2px; background: var(--white);
  }
  .phone { top: 220px; color: var(--sky); font-weight: 700; font-size: 35px; }
  .agent-name { top: 277px; color: var(--white); font-weight: 400; font-size: 31px; }
  .agent-title { top: 318px; color: var(--sky); font-weight: 400; font-size: 15px; }
  .agent-email { top: 358px; color: var(--white); font-weight: 400; font-size: 16.5px; }
  .license { top: 406px; color: var(--sky); font-weight: 300; font-size: 15.5px; }
  .badges {
    position: absolute; top: 447px; left: 0; width: 100%;
    display: flex; justify-content: center; gap: 18px;
  }
  .badge { width: 30px; height: 30px; background: var(--white); }
  .divider {
    position: absolute; top: 508px; left: 0; width: 100%;
    height: 2px; background: var(--rule);
  }
  .website { font-weight: 700; font-size: 17px; }
  .card--front .website { top: 542px; color: var(--sky); }

  .monogram-disc {
    position: absolute; left: 31px; top: 91px;
    width: 280px; height: 280px; border-radius: 50%;
    background: var(--espresso);
    display: flex; align-items: center; justify-content: center;
  }
  .monogram-disc span {
    font-family: "Cinzel", Georgia, serif; font-weight: 600;
    font-size: 96px; color: var(--sky); letter-spacing: 2px;
  }
  .card--back .website { top: 536px; color: var(--espresso); }
</style>
</head>
<body>
  <section class="card card--front">
    <div class="brand-dot"><span>TWL</span></div>
    <div class="centered brand-name">MARLOW</div>
    <div class="centered brand-sub">Realty Group</div>
    <div class="brand-llc">LLC</div>
    <div class="centered phone">816-552-4917</div>
    <div class="centered agent-name">Dorian Faulk</div>
    <div class="centered agent-title">Principal Broker</div>
    <div class="centered agent-email">dfaulk@marlowhomesexample.com</div>
    <div class="centered license">Licensed in the State of Missouri</div>
    <div class="badges">
      <div class="badge" role="img" aria-label="Trade association badge"></div>
      <div class="badge" role="img" aria-label="Fair housing badge"></div>
    </div>
    <div class="divider"></div>
    <div class="centered website">MarlowHomesExample.com</div>
  </section>

  <section class="card card--back">
    <div class="monogram-disc"><span>TWL</span></div>
    <div class="centered website">MarlowHomesExample.com</div>
  </section>
</body>
</html>
```